Business Card Design for a Personal Trainer

I need a business card design for my job as a personal trainer. It should have a unique, modern and exclusive design. On the front there should be only my logo with my name and my job. 0163/2918374 Tobias Kellinger Lindenfeldweg 14 80412 Munich Germany The most important contact information is the web adress. it can be bigger than the rest, but its not necessary. The card should be 8,5cmx5,5cm big. Font: Roboto. Colors: black, white, gray, 56c1ff.

```html
<!DOCTYPE html>
<html lang="de">
<head>
<meta charset="utf-8">
<title>Tobias Kellinger – Visitenkarte</title>
<link rel="stylesheet" href="https://fonts.googleapis.com/css2?family=Roboto:wght@700&family=Roboto+Condensed:wght@300;700&display=swap">
<style>
  :root {
    --blue: #56c1ff;
    --black: #000000;
    --white: #ffffff;
    --photo-light: #8a8a8a;
    --photo-dark: #2b2b2b;
  }
  html, body {
    margin: 0;
    padding: 0;
    overflow: hidden;
    background: var(--white);
  }
  .card {
    position: relative;
    width: 1200px;
    height: 777px;
    overflow: hidden;
    background: var(--white);
    font-family: "Roboto Condensed", "Roboto", sans-serif;
    color: var(--blue);
  }
  .card__backdrop {
    position: absolute;
    inset: 0;
    width: 1200px;
    height: 777px;
  }
  .card__portrait {
    position: absolute;
    left: 700px;
    top: 0;
    width: 500px;
    height: 777px;
    background: linear-gradient(180deg, var(--photo-light) 0%, #5a5a5a 35%, var(--photo-dark) 100%);
    clip-path: polygon(36% 0, 72% 0, 78% 28%, 100% 40%, 100% 100%, 10% 100%, 0 52%, 14% 36%, 34% 30%);
  }
  .card__rule {
    position: absolute;
    left: 260px;
    width: 462px;
    height: 3px;
    background: var(--blue);
  }
  .card__rule--top { top: 207px; }
  .card__rule--middle { top: 422px; }
  .card__rule--bottom { top: 586px; }
  .contact__line {
    position: absolute;
    left: 310px;
    margin: 0;
    font-size: 33px;
    line-height: 1;
    white-space: nowrap;
  }
  .contact__line--strong { font-weight: 700; }
  .contact__line--light { font-weight: 300; }
  .contact__name { top: 242px; }
  .contact__email { top: 298px; }
  .contact__phone { top: 351px; }
  .contact__street { top: 462px; }
  .contact__city { top: 518px; }
  .card__website {
    position: absolute;
    left: 48px;
    top: 642px;
    margin: 0;
    font-family: "Roboto", sans-serif;
    font-weight: 700;
    font-size: 71px;
    line-height: 1;
    letter-spacing: 1px;
    color: var(--blue);
    white-space: nowrap;
  }
</style>
</head>
<body>
  <main class="card">
    <svg class="card__backdrop" viewBox="0 0 1000 650" preserveAspectRatio="none" aria-hidden="true">
      <rect width="1000" height="650" fill="var(--white)"/>
      <polygon points="0,0 580,0 240,105 80,240 0,460" fill="var(--blue)"/>
      <polygon points="35,0 68,0 125,205" fill="var(--white)"/>
      <polygon points="215,0 450,0 245,100" fill="var(--white)"/>
      <polygon points="0,460 80,240 240,105 560,0 760,0 760,650 0,650" fill="var(--black)"/>
    </svg>

    <div class="card__portrait" role="img" aria-label="Black-and-white portrait of the trainer with arms crossed, wearing a dark athletic shirt"></div>

    <div class="card__rule card__rule--top"></div>
    <p class="contact__line contact__line--strong contact__name">Tobias Kellinger</p>
    <p class="contact__line contact__line--strong contact__email">t.kellinger@mailpost.de</p>
    <p class="contact__line contact__line--light contact__phone">0163/2918374</p>

    <div class="card__rule card__rule--middle"></div>
    <p class="contact__line contact__line--light contact__street">Lindenfeldweg 14</p>
    <p class="contact__line contact__line--light contact__city">80412 München</p>

    <div class="card__rule card__rule--bottom"></div>
    <p class="card__website">TOBIASKELLINGER.DE</p>
  </main>
</body>
</html>
```